Clearline Cable Mapping Format Sticker

We need a set of stickers (~5-7cm) to promote the Clearline Cable Mapping Format. Most of the people we will be handing these out to are technically minded (network operators, open-source coders, Internet standards folk, Internet measurement researchers). The design should include the CCMF icon and colour scheme (see here https://ccmf-example.org/en/resources/).

Target Market(s)

network operators, open-source coders, Internet standards folk, Internet measurement researchers

Font styles to use
Other font styles liked:
• Hind

```html
<!DOCTYPE html>
<html lang="en">
<head>
<meta charset="utf-8">
<title>Clearline Cable Mapping Format – Sticker Designs</title>
<link rel="stylesheet" href="https://fonts.googleapis.com/css2?family=Hind:wght@300;400;500;600&family=Montserrat:wght@700&display=swap">
<style>
  :root{
    --sheet:#d9d9d9;
    --ink:#14141c;
    --lime:#c8d42f;
    --white:#ffffff;
    --grey:#2b2b2e;
    --muted:#4b4870;
    --map-green:#1f5a3a;
    --map-violet:#3b2f6e;
  }
  *{box-sizing:border-box;margin:0;padding:0}
  html,body{width:1070px;height:1200px;overflow:hidden;background:var(--sheet)}
  body{position:relative;font-family:"Hind",sans-serif;color:var(--white)}
  .sheet-title{position:absolute;left:83px;top:92px;font:400 29px/1 "Hind",sans-serif;color:#1a1a1a}
  .sticker{position:absolute;width:256px;height:181px;border-radius:22px;background:var(--ink);border:3px solid var(--lime);overflow:hidden}
  .sticker > *{position:absolute}
  .tagline{font:700 13px/13.5px "Montserrat",sans-serif;color:var(--white);letter-spacing:-.2px}
  .wordmark{font:600 46px/1 "Hind",sans-serif;color:var(--white);letter-spacing:-1px}
  .name{font:400 12.5px/1 "Hind",sans-serif;color:var(--white);white-space:nowrap}
  .web{font:400 10.5px/1 "Hind",sans-serif;color:var(--lime);letter-spacing:1.2px;white-space:nowrap}
  .social{font:500 9px/1 "Hind",sans-serif;color:var(--white);display:flex;align-items:center;gap:3px}
  .social::before{content:"";width:8px;height:8px;border-radius:2px;background:var(--white)}
  .rule{height:2px;background:var(--lime)}
  .map-band{background:linear-gradient(100deg,var(--map-green),#111318 45%,var(--map-violet) 75%,#111318)}
  .line-field{background:linear-gradient(180deg,transparent,rgba(200,212,47,.18) 50%,transparent)}
  .node-area{border-radius:50%;background:radial-gradient(circle,rgba(200,212,47,.45),rgba(75,72,112,.35) 60%,transparent 72%)}
  .side-text{font:400 9px/1 "Hind",sans-serif;color:var(--lime);letter-spacing:1.2px;writing-mode:vertical-rl;white-space:nowrap}
  .side-text.up{transform:rotate(180deg)}
  .sticker.map-card{border:none;background:var(--grey)}
  .sticker.lime-card{background:var(--lime);border:none}
  .lime-card .tagline,.lime-card .wordmark,.lime-card .name,.lime-card .web{color:var(--ink)}
</style>
</head>
<body>

<h1 class="sheet-title">Sticker Designs 1</h1>

<!-- Row 1 -->
<div class="sticker" style="left:85px;top:173px">
  <p class="tagline" style="left:21px;top:23px">Mapping the<br>world's Internet<br>backbone.</p>
  <p class="wordmark" style="right:14px;top:30px">ccmf</p>
  <div class="map-band" role="img" aria-label="Dark network map of East African fibre routes" style="left:0;top:84px;width:100%;height:62px"></div>
  <p class="name" style="left:21px;top:110px">Clearline Cable Mapping Format</p>
  <p class="web" style="left:21px;top:158px">www.ccmf-example.org</p>
  <p class="social" style="right:12px;top:158px">Linkr</p>
</div>

<div class="sticker lime-card" style="left:416px;top:175px;width:254px;height:179px">
  <p class="tagline" style="left:22px;top:15px">Mapping the<br>world's Internet<br>backbone.</p>
  <p class="wordmark" style="right:18px;top:16px">ccmf</p>
  <div class="map-band" role="img" aria-label="Dark network map of East African fibre routes" style="left:0;top:64px;width:100%;height:64px;border-radius:18px"></div>
  <p class="name" style="left:22px;top:138px;font-size:14px">Clearline Cable Mapping Format</p>
  <p class="web" style="left:22px;top:157px">www.ccmf-example.org</p>
</div>

<div class="sticker map-card" style="left:725px;top:181px;width:253px;height:179px">
  <div role="img" aria-label="Dark network map of East African fibre routes" style="left:0;top:0;width:100%;height:100%;background:linear-gradient(118deg,#122018 0%,#1a1530 35%,#141a16 52%,transparent 53%)"></div>
  <p class="wordmark" style="right:20px;top:20px">ccmf</p>
  <p class="web" style="right:21px;top:64px">www.ccmf-example.org</p>
  <p class="tagline" style="left:17px;top:88px">Mapping the<br>world's Internet<br>backbone.</p>
  <div class="rule" style="left:17px;top:133px;width:102px"></div>
  <p class="name" style="left:17px;top:143px;font-size:11.5px">Clearline Cable Mapping Format</p>
</div>

<!-- Row 2 -->
<div class="sticker" style="left:84px;top:410px">
  <p class="tagline" style="left:21px;top:17px">Mapping the<br>world's Internet<br>backbone.</p>
  <p class="wordmark" style="right:16px;top:20px">ccmf</p>
  <div class="rule" style="left:21px;top:60px;width:96px"></div>
  <p class="name" style="left:21px;top:70px;font-size:11px">Clearline Cable Mapping Format</p>
  <div class="line-field" role="img" aria-label="Illustration of fibre strands running across the sticker" style="left:0;top:82px;width:100%;height:70px"></div>
  <p class="web" style="left:21px;top:158px">www.ccmf-example.org</p>
</div>

<div class="sticker" style="left:415px;top:412px">
  <div class="node-area" role="img" aria-label="Decorative network node illustration" style="left:80px;top:9px;width:84px;height:84px"></div>
  <p class="wordmark" style="left:0;width:100%;text-align:center;top:100px">ccmf</p>
  <p class="name" style="left:22px;width:190px;text-align:center;top:148px;font-size:12px">Clearline Cable Mapping Format</p>
  <p class="side-text" style="left:10px;top:26px">outreach@ccmf-example.org</p>
  <p class="side-text up" style="right:10px;top:26px">www.ccmf-example.org</p>
  <p class="social" style="right:10px;top:150px">Linkr</p>
</div>

<div class="sticker" style="left:723px;top:410px">
  <p class="tagline" style="left:18px;top:20px">Mapping the<br>world's Internet<br>backbone.</p>
  <p class="wordmark" style="right:16px;top:22px">ccmf</p>
  <div class="rule" style="left:18px;top:63px;width:97px"></div>
  <p class="name" style="left:18px;top:72px;font-size:11px">Clearline Cable Mapping Format</p>
  <p class="web" style="left:18px;top:111px;font-size:9px;letter-spacing:.8px">outreach@ccmf-example.org</p>
  <p class="web" style="left:18px;top:125px;font-size:10px;color:var(--white)">www.ccmf-example.org</p>
  <p class="social" style="left:18px;top:147px">Linkr</p>
  <div class="node-area" role="img" aria-label="Decorative network node illustration" style="left:160px;top:82px;width:84px;height:84px"></div>
</div>

<!-- Row 3 -->
<div class="sticker" style="left:87px;top:664px">
  <p class="side-text" style="left:9px;top:26px;font-size:9.5px">outreach@ccmf-example.org</p>
  <p class="side-text up" style="right:11px;top:26px;font-size:9.5px">www.ccmf-example.org</p>
  <p class="wordmark" style="left:0;width:100%;text-align:center;top:14px;font-size:84px;letter-spacing:-2px">ccmf</p>
  <p class="name" style="left:30px;width:196px;text-align:center;top:100px;font-size:22px;line-height:27px;white-space:normal">Clearline Cable Mapping Format</p>
  <p class="social" style="right:10px;top:150px">Linkr</p>
</div>

<!-- Row 4: round stickers -->
<svg style="position:absolute;left:85px;top:940px" width="184" height="184" viewBox="0 0 184 184">
  <defs>
    <radialGradient id="nodeGlow"><stop offset="0" stop-color="#c8d42f" stop-opacity=".45"/><stop offset=".6" stop-color="#4b4870" stop-opacity=".35"/><stop offset="1" stop-color="#4b4870" stop-opacity="0"/></radialGradient>
    <path id="arcL" d="M52 23 A80 80 0 0 0 52 161"/>
    <path id="arcR" d="M132 161 A80 80 0 0 0 132 23"/>
  </defs>
  <circle cx="92" cy="92" r="88" fill="var(--ink)" stroke="var(--lime)" stroke-width="7"/>
  <circle cx="92" cy="42" r="28" fill="url(#nodeGlow)" role="img" aria-label="Decorative network node illustration"/>
  <text x="92" y="114" text-anchor="middle" font-family="Hind,sans-serif" font-weight="600" font-size="44" fill="#fff" letter-spacing="-1">ccmf</text>
  <text x="92" y="129" text-anchor="middle" font-family="Hind,sans-serif" font-size="7.5" fill="var(--lime)" letter-spacing="1.6">CLEARLINE CABLE</text>
  <text x="92" y="140" text-anchor="middle" font-family="Hind,sans-serif" font-size="7.5" fill="var(--lime)" letter-spacing="1.6">MAPPING FORMAT</text>
  <rect x="82" y="154" width="7" height="7" rx="1.5" fill="#fff"/>
  <text x="92" y="161" font-family="Hind,sans-serif" font-size="8" font-weight="500" fill="#fff">Linkr</text>
  <text font-family="Hind,sans-serif" font-size="9" fill="var(--lime)" letter-spacing="1"><textPath href="#arcL" startOffset="50%" text-anchor="middle">outreach@ccmf-example.org</textPath></text>
  <text font-family="Hind,sans-serif" font-size="9" fill="var(--lime)" letter-spacing="1.2"><textPath href="#arcR" startOffset="50%" text-anchor="middle">www.ccmf-example.org</textPath></text>
</svg>

<svg style="position:absolute;left:297px;top:940px" width="184" height="184" viewBox="0 0 184 184">
  <defs>
    <radialGradient id="nodeGlow2"><stop offset="0" stop-color="#c8d42f" stop-opacity=".45"/><stop offset=".6" stop-color="#4b4870" stop-opacity=".35"/><stop offset="1" stop-color="#4b4870" stop-opacity="0"/></radialGradient>
    <path id="arcL2" d="M52 23 A80 80 0 0 0 52 161"/>
    <path id="arcR2" d="M132 161 A80 80 0 0 0 132 23"/>
  </defs>
  <circle cx="92" cy="92" r="88" fill="var(--ink)" stroke="var(--lime)" stroke-width="7"/>
  <circle cx="92" cy="36" r="23" fill="url(#nodeGlow2)" role="img" aria-label="Decorative network node illustration"/>
  <text x="92" y="88" text-anchor="middle" font-family="Hind,sans-serif" font-weight="600" font-size="30" fill="#fff" letter-spacing="-.6">ccmf</text>
  <text text-anchor="middle" font-family="Montserrat,sans-serif" font-weight="700" font-size="9.5" fill="#fff">
    <tspan x="92" y="102">Mapping the</tspan><tspan x="92" y="113">world's Internet</tspan><tspan x="92" y="124">backbone.</tspan>
  </text>
  <rect x="57" y="128" width="70" height="1.6" fill="var(--lime)"/>
  <text x="92" y="137" text-anchor="middle" font-family="Hind,sans-serif" font-size="6" fill="var(--lime)" letter-spacing="1.3">CLEARLINE CABLE</text>
  <text x="92" y="145" text-anchor="middle" font-family="Hind,sans-serif" font-size="6" fill="var(--lime)" letter-spacing="1.3">MAPPING FORMAT</text>
  <rect x="82" y="152" width="6" height="6" rx="1.3" fill="#fff"/>
  <text x="91" y="158" font-family="Hind,sans-serif" font-size="7" font-weight="500" fill="#fff">Linkr</text>
  <text font-family="Hind,sans-serif" font-size="9" fill="var(--lime)" letter-spacing="1"><textPath href="#arcL2" startOffset="50%" text-anchor="middle">outreach@ccmf-example.org</textPath></text>
  <text font-family="Hind,sans-serif" font-size="9" fill="var(--lime)" letter-spacing="1.2"><textPath href="#arcR2" startOffset="50%" text-anchor="middle">www.ccmf-example.org</textPath></text>
</svg>

<!-- Hexagons -->
<svg style="position:absolute;left:549px;top:949px" width="156" height="177" viewBox="0 0 156 177">
  <polygon points="78,0 156,44 156,133 78,177 0,133 0,44" fill="var(--ink)"/>
  <text x="78" y="73" text-anchor="middle" font-family="Hind,sans-serif" font-weight="600" font-size="54" fill="#fff" letter-spacing="-1.2">ccmf</text>
  <text x="78" y="103" text-anchor="middle" font-family="Hind,sans-serif" font-size="12" fill="var(--lime)" letter-spacing="1.2">CLEARLINE CABLE</text>
  <text x="78" y="118" text-anchor="middle" font-family="Hind,sans-serif" font-size="12" fill="var(--lime)" letter-spacing="1.2">MAPPING FORMAT</text>
  <text x="78" y="138" text-anchor="middle" font-family="Hind,sans-serif" font-size="10" fill="#fff" letter-spacing=".8">www.ccmf-example.org</text>
</svg>

<svg style="position:absolute;left:758px;top:937px" width="173" height="197" viewBox="0 0 173 197">
  <polygon points="86.5,3 170,51 170,146 86.5,194 3,146 3,51" fill="var(--ink)" stroke="var(--lime)" stroke-width="6"/>
  <text x="86.5" y="84" text-anchor="middle" font-family="Hind,sans-serif" font-weight="600" font-size="56" fill="#fff" letter-spacing="-1.2">ccmf</text>
  <text x="86.5" y="114" text-anchor="middle" font-family="Hind,sans-serif" font-size="12.5" fill="var(--lime)" letter-spacing="1.2">CLEARLINE CABLE</text>
  <text x="86.5" y="129" text-anchor="middle" font-family="Hind,sans-serif" font-size="12.5" fill="var(--lime)" letter-spacing="1.2">MAPPING FORMAT</text>
  <text x="86.5" y="150" text-anchor="middle" font-family="Hind,sans-serif" font-size="10.5" fill="#fff" letter-spacing=".8">www.ccmf-example.org</text>
</svg>

</body>
</html>
```